Modern Billboard Ad for Criminal Defense Firm

10.5 x 36 We're looking for something to set us apart from the local competition. Looking for sleek and modern. We're a mid-sized firm in a small market city. We want to give the artist room to be creative on this one.
Thanks

Target Market(s)

Adult clients who have been charged with a crime/DWI

Industry/Entity Type

legal

Font styles to use
Serif
Sans Serif

Requirements
Must have
• Needs to have the firm name in large lettering. Law Offices of Marcus T Whitfield. “PLLC” does not have to be included. Phone number of (555) 384-1927 should be included but not the main focus.
Nice to have
• A call to action or something similar. “Don’t go it alone, call today.”, “ Arrested?”

```html
<!DOCTYPE html>
<html lang="en">
<head>
<meta charset="utf-8">
<title>Law Offices of Marcus T Whitfield – Billboard</title>
<link rel="stylesheet" href="https://fonts.googleapis.com/css2?family=Anton&family=Montserrat:wght@800;900&display=swap">
<style>
  :root {
    --navy: #0b3670;
    --navy-deep: #082a5c;
    --sky: #1b8fd2;
    --yellow: #ffc800;
    --red: #e5202e;
    --white: #ffffff;
    --stage: #eef1f5;
    --shirt: #e9ecef;
    --suit: #7d8085;
  }
  html, body {
    margin: 0;
    width: 1200px;
    height: 1042px;
    overflow: hidden;
    background: var(--stage);
  }
  .billboard {
    position: absolute;
    left: 0;
    top: 346px;
    width: 1200px;
    height: 350px;
    display: block;
  }
  .title-line-1 { font-family: "Anton", "Impact", sans-serif; fill: var(--yellow); }
  .title-line-2 { font-family: "Anton", "Impact", sans-serif; fill: var(--white); }
  .tagline { font-family: "Montserrat", "Arial", sans-serif; font-weight: 800; font-size: 25px; fill: var(--white); }
  .tagline-accent { fill: var(--yellow); }
  .phone { font-family: "Montserrat", "Arial", sans-serif; font-weight: 800; font-size: 29px; fill: var(--red); }
  .website { font-family: "Montserrat", "Arial", sans-serif; font-weight: 800; font-size: 27px; fill: var(--navy-deep); }
</style>
</head>
<body>
<svg class="billboard" viewBox="0 0 1200 350" xmlns="http://www.w3.org/2000/svg">
  <defs>
    <radialGradient id="board-bg" cx="0.55" cy="0.45" r="0.75">
      <stop offset="0" stop-color="#0a2f66"/>
      <stop offset="0.55" stop-color="#0e4a8e"/>
      <stop offset="1" stop-color="#1b8fd2"/>
    </radialGradient>
    <linearGradient id="client-photo" x1="0" y1="0" x2="0" y2="1">
      <stop offset="0" stop-color="#5a3a26"/>
      <stop offset="0.3" stop-color="#d9a88a"/>
      <stop offset="0.45" stop-color="#eef0f2"/>
      <stop offset="1" stop-color="#dfe3e8"/>
    </linearGradient>
    <linearGradient id="attorney-photo" x1="0" y1="0" x2="0" y2="1">
      <stop offset="0" stop-color="#3a2e26"/>
      <stop offset="0.3" stop-color="#d8a98e"/>
      <stop offset="0.48" stop-color="#8a8d92"/>
      <stop offset="1" stop-color="#6e7176"/>
    </linearGradient>
  </defs>

  <!-- board background -->
  <rect class="board-bg" width="1200" height="350" fill="url(#board-bg)"/>

  <!-- torn paper band -->
  <polygon class="torn-edge" fill="var(--white)"
    points="0,292 40,284 80,290 130,278 200,272 250,262 300,266 340,258 380,268 420,260 470,266 520,256 570,264 620,262 660,254 700,262 760,256 810,262 860,254 905,258 905,350 0,350"/>
  <polygon class="yellow-band" fill="var(--yellow)"
    points="0,298 45,291 85,296 135,285 205,279 255,270 305,274 345,266 385,276 425,268 475,274 525,264 575,272 625,270 665,262 705,270 765,264 815,270 865,262 905,266 905,350 0,350"/>

  <!-- client photo area -->
  <rect class="client-photo" x="42" y="10" width="252" height="340" rx="6" fill="url(#client-photo)"
        role="img" aria-label="Photo of a worried man in shirt and tie, hands cuffed, shrugging"/>

  <!-- attorney photo area -->
  <rect class="attorney-photo" x="968" y="14" width="232" height="336" rx="6" fill="url(#attorney-photo)"
        role="img" aria-label="Portrait of the attorney smiling in a grey plaid suit"/>

  <!-- firm name -->
  <text class="title-line-1" x="309" y="98" font-size="96" textLength="616" lengthAdjust="spacingAndGlyphs">LAW OFFICES OF</text>
  <text class="title-line-2" x="309" y="197" font-size="98" textLength="622" lengthAdjust="spacingAndGlyphs">MARCUS T WHITFIELD</text>

  <!-- call to action strip -->
  <g class="cta" transform="rotate(-1.6 620 224)">
    <rect x="348" y="201" width="546" height="44" fill="var(--red)"/>
    <text class="tagline" x="370" y="233" textLength="504" lengthAdjust="spacingAndGlyphs">DON’T GO IT ALONE, <tspan class="tagline-accent">CALL TODAY!</tspan></text>
  </g>

  <!-- award badge -->
  <g class="award-badge">
    <rect x="903" y="244" width="64" height="92" fill="var(--navy)" stroke="var(--white)" stroke-width="2"/>
    <rect x="907" y="320" width="56" height="12" fill="var(--sky)"/>
  </g>

  <!-- contact line -->
  <text class="phone" x="289" y="330">(555) 384-1927</text>
  <rect class="divider" x="548" y="302" width="3" height="34" fill="var(--red)"/>
  <text class="website" x="565" y="330" textLength="330" lengthAdjust="spacingAndGlyphs">www.whitfieldfirm.com</text>
</svg>
</body>
</html>
```